Designing a brochures for an educational counseling service provider

We would like a 4 sided design on a 11x8.5 paper, half folded. I have including a sample design we did to give you an idea of what we envision but we welcome creativity to make beautiful looking flyers. Text for the flier is included as well as our logo.
- The most important thing is capturing our audience/market. We will be handing these flies to schools, organizations and individual clients.

www.plorvaeducationalconsultants.example

Target Market(s)

We are targeting international students wanting to study in the U.S and Canada.

Industry/Entity Type

Education

Requirements
Must have
• - Clean and clear
• - Our logo should visible and well placed.
• - Could you the pictures of students, libraries and school buildings or you could use the pictures we already have.
Nice to have
• We would like this to match business cards.

```html
<!DOCTYPE html>
<html lang="en">
<head>
<meta charset="utf-8">
<title>Plorva Educational Consultants – Folder Spread</title>
<link rel="stylesheet" href="https://fonts.googleapis.com/css2?family=Montserrat:wght@500;600;700&family=Ubuntu:wght@500&display=swap">
<style>
  :root {
    --navy: #0f1e3a;
    --teal: #1794a6;
    --teal-text: #2ba3bd;
    --sky: #7ab6d0;
    --slate: #5d6170;
    --paper: #ffffff;
    --backdrop: #e4e5e7;
    --ink: #1c1f26;
  }
  * { box-sizing: border-box; margin: 0; padding: 0; }
  html, body { width: 1200px; height: 1200px; overflow: hidden; }
  body { background: var(--backdrop); position: relative; font-family: "Montserrat", sans-serif; }

  .spread { position: absolute; left: 100px; top: 214px; width: 1000px; height: 773px; display: flex; box-shadow: 0 8px 30px rgba(0,0,0,.15); }
  .panel { position: relative; width: 500px; height: 773px; background: var(--paper); overflow: hidden; }
  .panel svg.shapes, .panel svg.photo { position: absolute; inset: 0; width: 100%; height: 100%; }

  .brand { position: absolute; display: flex; align-items: center; gap: 8px; }
  .brand-dot { width: 22px; height: 22px; border-radius: 50%; background: var(--teal); }
  .brand-name { font-family: "Montserrat", sans-serif; font-weight: 700; color: var(--navy); letter-spacing: .5px; }

  /* back panel */
  .back .brand { left: 60px; top: 150px; }
  .back .brand-name { font-size: 22px; }
  .contact-block { position: absolute; left: 0; right: 0; top: 405px; text-align: center; }
  .contact-title { color: #fff; font-weight: 600; font-size: 16px; letter-spacing: 1px; margin-bottom: 8px; }
  .contact-lines { color: var(--teal-text); font-weight: 500; font-size: 12.5px; line-height: 1.45; letter-spacing: .4px; text-transform: uppercase; }
  .reach { position: absolute; right: 36px; top: 616px; text-align: right; color: var(--ink); font-weight: 700; font-size: 11.5px; line-height: 1.7; letter-spacing: .2px; text-transform: uppercase; }

  /* front panel */
  .tagline { position: absolute; left: 0; right: 0; top: 30px; text-align: center; font-family: "Ubuntu", sans-serif; font-weight: 500; font-size: 15.5px; line-height: 1.25; color: var(--ink); }
  .front .brand-main { left: 225px; top: 100px; }
  .front .brand-main .brand-dot { width: 30px; height: 30px; }
  .front .brand-main .brand-name { font-size: 30px; }
  .front .brand-foot { left: 255px; top: 708px; }
  .front .brand-foot .brand-dot { width: 18px; height: 18px; }
  .front .brand-foot .brand-name { font-size: 18px; }
</style>
</head>
<body>
  <main class="spread">
    <section class="panel back">
      <svg class="shapes" viewBox="0 0 500 773" aria-hidden="true">
        <path d="M500 0 L455 0 C395 170 220 300 0 330 L0 346 C240 332 430 205 500 92 Z" fill="var(--teal)"/>
        <path d="M500 140 C430 262 250 372 0 378 L0 572 C160 604 350 602 500 556 Z" fill="var(--navy)"/>
        <path d="M0 664 L0 773 L60 773 C110 732 180 702 262 682 C170 684 80 676 0 664 Z" fill="var(--teal)"/>
        <path d="M100 773 C150 740 220 712 300 692 C222 726 172 750 150 773 Z" fill="var(--navy)"/>
      </svg>
      <div class="brand"><span class="brand-dot"></span><span class="brand-name">Plorva</span></div>
      <div class="contact-block">
        <h2 class="contact-title">CONTACT US</h2>
        <p class="contact-lines">Executive Director &amp; Independent<br>Educational Consultant<br>Plorva International Educational Consultants, LLC<br>1480 Meridian Rd<br>Suite 310B, Oakmere, TX 75555</p>
      </div>
      <p class="reach">Phone: 555-014-2290<br>Email: mara@plorvaeducationalconsultants.example</p>
    </section>

    <section class="panel front">
      <svg class="photo" viewBox="0 0 500 773" role="img" aria-label="Photograph of two smiling students posing together">
        <defs>
          <linearGradient id="studentTones" x1="0" y1="0" x2="1" y2="1">
            <stop offset="0" stop-color="#b38f78"/>
            <stop offset=".45" stop-color="#6f5b52"/>
            <stop offset="1" stop-color="#4f6477"/>
          </linearGradient>
        </defs>
        <path d="M0 90 C150 120 320 200 500 330 L500 560 C340 522 150 560 0 592 Z" fill="url(#studentTones)"/>
      </svg>
      <svg class="shapes" viewBox="0 0 500 773" aria-hidden="true">
        <path d="M0 70 C150 100 330 185 500 310 L500 332 C320 202 150 120 0 92 Z" fill="var(--slate)"/>
        <path d="M300 236 C380 244 450 262 500 280 L500 300 C440 272 370 252 300 236 Z" fill="var(--teal)"/>
        <path d="M380 226 L500 216 L500 242 C460 234 420 229 380 226 Z" fill="var(--navy)"/>
        <path d="M0 560 C160 548 320 560 500 520 L500 548 C330 600 160 604 0 612 Z" fill="var(--navy)"/>
        <path d="M170 600 C300 590 420 570 500 545 L500 565 C400 600 280 612 170 600 Z" fill="var(--sky)"/>
      </svg>
      <p class="tagline">A full-service international consulting group<br>serving students and families across the globe.</p>
      <div class="brand brand-main"><span class="brand-dot"></span><span class="brand-name">Plorva</span></div>
      <div class="brand brand-foot"><span class="brand-dot"></span><span class="brand-name">Plorva</span></div>
    </section>
  </main>
</body>
</html>
```